UI Design for a pre-ordering & Universal loyalty mobile app

We have built a central universal, preordering and gamification mobile app for alot of F&B merchant. The app is called TRIVU (Trivoo as in eating something fast). Main goal for this app is too
1. Give users a universal loyalty system where they can accumulate loyalty points and use it on any brands
2. Gives user the ability to preorder for their food or drinks on the app and pick it up instore
3. There will be an E-wallet that is general or there can be a brand e-wallet (where they top-up with the brand only and get extra bonus)
4. There will be promotion such as games, top-up bonuses and rewards.
5. Community app where they can send money or promotion to their friends and will be able to play games together
This app is developed on the Flutter framework and also uses fontawesome font/icon package. Please consider this when doing the UI design for the app.
We are planning to create a mascot for our app as well and when it comes to color and icon, it's not set in stone and we are open for ideas.
I will attached our app icon and a few of our screens for your reference and each page details as follows:
Navigation bar.
There is a navigation bar on the top that should be visible on all screen. On the left will be a button to enter the menu which gives user more option and on the right will be a place for them to scan their QR code for loyalty points or payment and also a button to access their e-wallet.
1. Home screen
This screen is basically the main screen after user login. In this screen there will be
- Main banner (main promotions that's controlled by us)
- Specials banner (smaller) that will be controlled by the store/brands
- Favourite Store or Favourite food/drinks that user pre-configure
2. Shop screen (or can be called something else)
This screen is where they can browse all our participating stores. This screen will include
- Categories (filter)
- Brands which user can click and only view the brand page and stores
- All stores sorted by distances
3. Brand screen
The brand screen gives our brand with multiple store a presense on the app that is branded for them. They can have their own color scheme, logo and will only display their own store
4. Store screen
This will display all the store details, opening time, location, contact information etc.
- This screen will contain a banner/store image
- Store details
- Categories
- Food/drinks within the category
5. Order history screen
This will display their current order or their past order. Not sure if it should be on the main navigation or the sub navigation.
When making the UI design, please work on a color theme that will suit and also consider a mascot design in the future.
Feel free to ask me any questions before proceeding.
Thanks

```html
<!DOCTYPE html>
<html lang="en">
<head>
<meta charset="utf-8">
<title>TRIVU – App design, 6 screens</title>
<link href="https://fonts.googleapis.com/css2?family=Inter:wght@400;500;600;700;800&display=swap" rel="stylesheet">
<style>
:root{
  --bg:#f3f3f3;
  --brand:#8cc63f;
  --brand-bright:#7dcc2e;
  --brand-soft:#e9f6da;
  --ink:#1e1e1e;
  --ink-2:#3a3a3a;
  --muted:#a9a9a9;
  --line:#ececec;
  --nav-idle:#d2d2d2;
  --device:#f1f1f1;
  --device-edge:#e3e3e3;
  --card:#ffffff;
}
*{box-sizing:border-box;margin:0;padding:0}
html,body{width:1200px;height:1042px;overflow:hidden;background:var(--bg);font-family:"Inter",Arial,sans-serif;color:var(--ink)}
.board{position:relative;width:1200px;height:1042px;overflow:hidden;background:var(--bg)}
.abs{position:absolute}
svg.icon{display:block}

/* left title block */
.brand-title{position:absolute;left:22px;top:126px;font-size:98px;font-weight:700;letter-spacing:1px;color:var(--brand);line-height:1}
.app-title{position:absolute;left:22px;top:252px;font-size:58px;font-weight:700;color:var(--ink);line-height:1;letter-spacing:-.5px}
.screen-count{position:absolute;left:22px;top:324px;font-size:34px;font-weight:600;color:var(--ink);line-height:1}
.accent-panel{position:absolute;left:0;top:514px;width:326px;height:560px;background:#9ac854;border-top-right-radius:96px}
.wand-badge{position:absolute;left:235px;top:475px;width:91px;height:91px;border-radius:50%;background:#fff;display:flex;align-items:center;justify-content:center}

/* device frames */
.device{position:absolute;width:215px;height:437px;border-radius:30px;background:var(--device);border:1px solid var(--device-edge)}
.screen{position:absolute;left:12px;top:12px;width:190px;height:411px;border-radius:20px;background:#fff;overflow:hidden}
.status{position:absolute;left:12px;top:7px;right:12px;display:flex;justify-content:space-between;align-items:center;font-size:7px;font-weight:600}
.status-icons{display:flex;gap:2px;align-items:center}

.header-greeting{position:absolute;left:8px;top:32px;right:8px;display:flex;align-items:center}
.avatar{width:18px;height:18px;border-radius:50%;background:#cfd8dc;border:1.5px solid var(--brand)}
.greeting{margin-left:7px;font-size:8px;font-weight:600;flex:1}
.round-btn{width:18px;height:18px;border-radius:50%;border:1px solid var(--line);display:flex;align-items:center;justify-content:center;background:#fff}
.header-greeting .round-btn+.round-btn{margin-left:10px}

.header-title{position:absolute;left:8px;right:8px;top:31px;display:flex;align-items:center;justify-content:space-between}
.header-title h2{font-size:10px;font-weight:500;color:var(--ink)}

.section-title{position:absolute;left:8px;font-size:7.5px;font-weight:600;color:var(--ink)}
.see-all{position:absolute;right:8px;font-size:4.5px;font-weight:600;color:var(--brand-bright)}

.photo{border-radius:6px}
.photo-cafe{background:linear-gradient(160deg,#5a4a3c 0%,#8a6d52 40%,#3c3f3a 75%,#2a2a28 100%)}
.photo-drinks{background:linear-gradient(135deg,#9fb5a0 0%,#c8d2c4 45%,#a5b8a6 100%)}
.photo-deal-red{background:linear-gradient(110deg,#d7e84b 0%,#7bc043 35%,#e2231a 60%,#b51712 100%)}
.photo-deal-coffee{background:linear-gradient(135deg,#5a1a14 0%,#a2261d 50%,#3a120d 100%)}
.photo-cup{background:linear-gradient(180deg,#f2ece6 0%,#d9c4ad 50%,#8a6a52 100%)}
.photo-cup-amber{background:linear-gradient(180deg,#f5f1ee 0%,#e26a1f 45%,#a22a12 100%)}
.photo-cup-red{background:linear-gradient(180deg,#f5f1ee 0%,#e03040 50%,#8d1420 100%)}
.photo-storefront{background:linear-gradient(160deg,#40464a 0%,#6e6256 50%,#2e302f 100%)}

/* favourites cards */
.fav-card{position:absolute;top:273px;height:81px;background:#fff;border-radius:6px;box-shadow:0 1px 4px rgba(0,0,0,.07);overflow:hidden}
.fav-card .photo{height:54px;border-radius:6px 6px 0 0}
.fav-card .meta{padding:2px 4px;font-size:3px;color:#555;line-height:1.8}
.fav-card .meta b{font-weight:500;font-size:3.4px;color:var(--ink)}
.mini-pill{position:absolute;left:4px;top:45px;background:var(--brand);color:#fff;font-size:2.4px;border-radius:3px;padding:1px 3px}
.mini-heart{position:absolute;left:5px;top:4px;width:9px;height:9px;border-radius:50%;border:1px solid #fff}
.mini-rate{position:absolute;right:3px;top:4px;background:#fff;border-radius:4px;font-size:3px;padding:1px 3px}

/* bottom nav */
.tabbar{position:absolute;left:0;right:0;bottom:0;height:42px;background:#fff;box-shadow:0 -8px 14px rgba(255,255,255,.9)}
.tab{position:absolute;top:11px;width:40px;margin-left:-20px;display:flex;flex-direction:column;align-items:center;font-size:5px;color:var(--nav-idle)}
.tab svg{margin-bottom:3px}
.tab.active{color:var(--brand-bright)}

/* store screen */
.info-row{position:absolute;left:8px;display:flex;align-items:center;gap:5px;font-size:5.5px;color:var(--ink-2)}
.info-row .faint{color:var(--muted)}
.chip{position:absolute;height:14px;border:1px solid var(--brand);border-radius:3px;color:var(--brand);font-size:6px;display:flex;align-items:center;justify-content:center}
.chip.filled{background:var(--brand);color:#fff}
.chip.plain{border:none;background:#f6f6f6;color:var(--muted);border-radius:3px}

.menu-item{position:absolute;left:8px;width:178px;height:56px;background:#fff;border-radius:6px;box-shadow:0 1px 5px rgba(0,0,0,.06)}
.menu-item .photo{position:absolute;left:4px;top:7px;width:41px;height:41px;border-radius:6px}
.menu-item .name{position:absolute;left:51px;top:10px;font-size:6.5px;font-weight:500}
.menu-item .desc{position:absolute;left:51px;top:22px;font-size:5px;color:var(--muted)}
.menu-item .price{position:absolute;left:51px;top:33px;font-size:7px;font-weight:500;color:var(--brand-bright)}
.menu-item .rate{position:absolute;right:6px;top:9px;font-size:5.5px;color:var(--ink-2);display:flex;gap:2px;align-items:center}
.menu-item .fav-dot{position:absolute;right:7px;bottom:8px;width:9px;height:9px;border-radius:50%;background:var(--brand-bright)}

/* order history */
.tabs{position:absolute;left:10px;width:171px;top:72px;height:22px;border-bottom:1px solid var(--line);display:flex}
.tabs span{flex:1;text-align:center;font-size:8.5px;color:var(--muted);position:relative}
.tabs span.on{color:var(--brand-bright)}
.tabs span.on::after{content:"";position:absolute;left:0;right:0;bottom:-9px;height:1.5px;background:var(--brand-bright)}
.order-card{position:absolute;background:#fff;border-radius:7px;box-shadow:0 2px 8px rgba(0,0,0,.06)}
.order-card .photo{position:absolute;width:45px;height:45px;border-radius:6px}
.order-card .name{position:absolute;font-size:7.5px;font-weight:500}
.order-card .desc{position:absolute;font-size:5px;color:var(--muted)}
.order-card .price{position:absolute;font-size:7.5px;font-weight:500;color:var(--brand-bright);display:flex;align-items:center;gap:4px}
.badge{background:var(--brand-bright);color:#fff;font-size:3px;font-weight:400;border-radius:1.5px;padding:1.5px 4px}
.btn{position:absolute;height:14px;border-radius:8px;font-size:6px;display:flex;align-items:center;justify-content:center}
.btn.outline{border:1px solid var(--brand-bright);color:var(--brand-bright);background:#fff}
.btn.solid{background:var(--brand-bright);color:#fff}

/* brand screen */
.brand-ring{position:absolute;left:50px;top:60px;width:88px;height:88px;border-radius:50%;border:5px solid var(--brand);display:flex;align-items:center;justify-content:center;font-size:13px;font-weight:700;color:var(--ink)}
.arrow-btn{position:absolute;width:15px;height:15px;border-radius:50%;display:flex;align-items:center;justify-content:center}
.story-card{position:absolute;left:8px;top:188px;width:173px;height:127px;border-radius:7px;background:#fff;box-shadow:0 2px 8px rgba(0,0,0,.07);overflow:hidden}
.story-card .photo{height:81px;border-radius:7px 7px 0 0}
.heart-badge{position:absolute;width:14px;height:14px;border-radius:50%;background:var(--brand-bright);border:1.5px solid #fff}
.rate-badge{position:absolute;background:#fff;border-radius:6px;font-size:5px;padding:2px 4px;display:flex;gap:2px;align-items:center}
.bonus-pill{position:absolute;background:var(--brand-bright);color:#fff;border-radius:4px;font-size:3.6px;padding:1.5px 4px}
.tags{display:flex;gap:6px;font-size:3px;color:var(--muted)}
.tags span{background:#f4f4f4;padding:1px 3px;border-radius:2px}
.loc{display:flex;align-items:center;gap:3px;font-size:4.5px;color:var(--ink-2)}
.eta{display:flex;align-items:center;gap:3px;font-size:4px;color:var(--muted)}

/* shop screen */
.search{position:absolute;left:7px;top:61px;width:141px;height:24px;border-radius:6px;background:#f6f6f6;display:flex;align-items:center;gap:5px;padding-left:8px;font-size:6px;color:var(--muted)}
.filter-btn{position:absolute;left:154px;top:61px;width:24px;height:24px;border-radius:6px;background:#fff;box-shadow:0 1px 5px rgba(0,0,0,.08);display:flex;align-items:center;justify-content:center}
.brand-dot{position:absolute;top:152px;width:20px;height:20px;border-radius:50%}
.store-row{position:absolute;left:7px;width:171px;height:46px;background:#fff;border-radius:5px;box-shadow:0 1px 5px rgba(0,0,0,.06)}
.store-row .photo{position:absolute;left:0;top:0;width:53px;height:46px;border-radius:5px}
.store-row .body{position:absolute;left:59px;top:5px;display:flex;flex-direction:column;gap:3px}
.store-row .body b{font-size:6px;font-weight:500}
.store-row .heart-badge{left:3px;top:3px;width:8px;height:8px;border-width:1px}
.store-row .rate-badge{left:38px;top:3px;font-size:2.6px;padding:1px 2px;border-radius:3px}
</style>
</head>
<body>
<svg width="0" height="0" style="position:absolute" aria-hidden="true">
  <defs>
    <symbol id="i-home" viewBox="0 0 24 24"><path d="M3 11 12 3l9 8v9a2 2 0 0 1-2 2H5a2 2 0 0 1-2-2z" fill="currentColor"/></symbol>
    <symbol id="i-cart" viewBox="0 0 24 24"><path d="M2 4h3l2.4 10h11L21 7H7" fill="none" stroke="currentColor" stroke-width="2.4" stroke-linejoin="round"/><path d="M7 7h14l-2.6 7H8.2z" fill="currentColor"/><circle cx="9" cy="19" r="1.8" fill="currentColor"/><circle cx="17" cy="19" r="1.8" fill="currentColor"/></symbol>
    <symbol id="i-doc" viewBox="0 0 24 24"><path d="M5 3h10l4 4v14H5z" fill="currentColor"/><path d="M8 11h8M8 15h6" stroke="#fff" stroke-width="1.6"/></symbol>
    <symbol id="i-user" viewBox="0 0 24 24"><circle cx="12" cy="8" r="4.5" fill="currentColor"/><path d="M3.5 21c1-4.5 4.5-7 8.5-7s7.5 2.5 8.5 7z" fill="currentColor"/></symbol>
    <symbol id="i-back" viewBox="0 0 24 24"><path d="M19 12H5m6-6-6 6 6 6" fill="none" stroke="currentColor" stroke-width="2" stroke-linecap="round" stroke-linejoin="round"/></symbol>
    <symbol id="i-more" viewBox="0 0 24 24"><circle cx="12" cy="5" r="2" fill="currentColor"/><circle cx="12" cy="12" r="2" fill="currentColor"/><circle cx="12" cy="19" r="2" fill="currentColor"/></symbol>
    <symbol id="i-pin" viewBox="0 0 24 24"><path d="M12 2a7 7 0 0 0-7 7c0 5 7 13 7 13s7-8 7-13a7 7 0 0 0-7-7z" fill="currentColor"/><circle cx="12" cy="9" r="2.6" fill="#fff"/></symbol>
    <symbol id="i-star" viewBox="0 0 24 24"><path d="m12 2 3 6.5 7 .8-5.2 4.8 1.4 7L12 17.6 5.8 21l1.4-7L2 9.3l7-.8z" fill="currentColor"/></symbol>
    <symbol id="i-clock" viewBox="0 0 24 24"><circle cx="12" cy="12" r="10" fill="currentColor"/><path d="M12 7v5l3 2" stroke="#fff" stroke-width="2" fill="none"/></symbol>
    <symbol id="i-map" viewBox="0 0 24 24"><path d="M2 5l6-2 8 3 6-2v15l-6 2-8-3-6 2z" fill="currentColor"/></symbol>
    <symbol id="i-store" viewBox="0 0 24 24"><path d="M3 9 5 4h14l2 5v2H3z" fill="currentColor"/><path d="M5 12h14v8H5z" fill="currentColor"/></symbol>
    <symbol id="i-heart" viewBox="0 0 24 24"><path d="M12 20s-7-4.5-7-10a4 4 0 0 1 7-2.5A4 4 0 0 1 19 10c0 5.5-7 10-7 10z" fill="none" stroke="currentColor" stroke-width="2"/></symbol>
    <symbol id="i-scan" viewBox="0 0 24 24"><path d="M4 8V5a1 1 0 0 1 1-1h3M16 4h3a1 1 0 0 1 1 1v3M20 16v3a1 1 0 0 1-1 1h-3M8 20H5a1 1 0 0 1-1-1v-3M3 12h18" fill="none" stroke="currentColor" stroke-width="1.8" stroke-linecap="round"/></symbol>
    <symbol id="i-wallet" viewBox="0 0 24 24"><rect x="3" y="6" width="18" height="14" rx="3" fill="none" stroke="currentColor" stroke-width="1.8"/><path d="M14 13h7" stroke="currentColor" stroke-width="1.8"/><circle cx="19" cy="5" r="2.6" fill="#ff4d4d"/></symbol>
    <symbol id="i-search" viewBox="0 0 24 24"><circle cx="11" cy="11" r="7" fill="none" stroke="currentColor" stroke-width="2"/><path d="m16 16 5 5" stroke="currentColor" stroke-width="2" stroke-linecap="round"/></symbol>
    <symbol id="i-filter" viewBox="0 0 24 24"><path d="M4 8h16M4 16h16" stroke="currentColor" stroke-width="2" stroke-linecap="round"/><circle cx="15" cy="8" r="2.6" fill="currentColor"/><circle cx="9" cy="16" r="2.6" fill="currentColor"/></symbol>
    <symbol id="i-chev-l" viewBox="0 0 24 24"><path d="m14 6-6 6 6 6" fill="none" stroke="currentColor" stroke-width="2.4" stroke-linecap="round" stroke-linejoin="round"/></symbol>
    <symbol id="i-chev-r" viewBox="0 0 24 24"><path d="m10 6 6 6-6 6" fill="none" stroke="currentColor" stroke-width="2.4" stroke-linecap="round" stroke-linejoin="round"/></symbol>
    <symbol id="i-signal" viewBox="0 0 34 10"><rect x="0" y="6" width="2.5" height="4" rx=".6"/><rect x="3.5" y="4" width="2.5" height="6" rx=".6"/><rect x="7" y="2" width="2.5" height="8" rx=".6"/><rect x="10.5" y="0" width="2.5" height="10" rx=".6"/><path d="M15 4a7 7 0 0 1 9 0l-1 1.2a5.4 5.4 0 0 0-7 0zM17 6.3a4 4 0 0 1 5 0l-2.5 3z"/><rect x="26" y="1.5" width="8" height="7" rx="1.5"/></symbol>
  </defs>
</svg>

<main class="board">
  <!-- title block -->
  <h1 class="brand-title">TRIVU</h1>
  <p class="app-title">App design</p>
  <p class="screen-count">6 Screen</p>
  <div class="accent-panel"></div>
  <div class="wand-badge">
    <svg class="icon" width="58" height="62" viewBox="0 0 58 62" fill="none" stroke="#222" stroke-width="3.2" stroke-linejoin="round">
      <path d="M12 54 47 13a5 5 0 0 1 7 6L19 60a5 5 0 0 1-7-6z"/>
      <path d="M39 22l7 6"/>
      <path d="M16 4l2 4 4 2-4 2-2 4-2-4-4-2 4-2z"/>
      <path d="M8 20l2 4 4 2-4 2-2 4-2-4-4-2 4-2z"/>
      <path d="M50 34l2 4 4 2-4 2-2 4-2-4-4-2 4-2z"/>
    </svg>
  </div>

  <!-- Screen 1: Home -->
  <section class="device" style="left:411px;top:59px">
    <div class="screen">
      <div class="status"><span>9:41</span><svg class="icon" width="30" height="8" fill="#1e1e1e"><use href="#i-signal"/></svg></div>
      <div class="header-greeting">
        <div class="avatar" role="img" aria-label="User avatar photo"></div>
        <span class="greeting">Hii, Amir</span>
        <span class="round-btn"><svg class="icon" width="10" height="10" color="#333"><use href="#i-scan"/></svg></span>
        <span class="round-btn"><svg class="icon" width="10" height="10" color="#333"><use href="#i-wallet"/></svg></span>
      </div>
      <p class="section-title" style="top:62px">Special Offers</p>
      <p class="see-all" style="top:64px">See All</p>
      <div class="abs photo photo-drinks" style="left:8px;top:84px;width:174px;height:87px" role="img" aria-label="Promotional banner of five flavoured drink cups on a leafy background"></div>
      <p class="section-title" style="top:179px">Deal</p>
      <p class="see-all" style="top:181px">See All</p>
      <div class="abs photo photo-deal-red" style="left:8px;top:195px;width:116px;height:56px" role="img" aria-label="Deal banner with coconut and boba drink"></div>
      <div class="abs photo photo-deal-coffee" style="left:130px;top:195px;width:70px;height:56px" role="img" aria-label="Deal banner with a free small coffee cup"></div>
      <p class="section-title" style="top:258px;left:9px">Favorites</p>
      <p class="see-all" style="top:261px">See All</p>
      <article class="fav-card" style="left:8px;width:102px">
        <div class="photo photo-cafe" role="img" aria-label="Cafe interior with wooden tables"></div>
        <span class="mini-heart"></span><span class="mini-rate">★ 4.2</span><span class="mini-pill">100% Deposit Bonus</span>
        <div class="meta"><b>Demo 2 Eastvale</b><br>Tea · Bubble Tea · Burger<br><span style="color:var(--brand)">●</span> 123 A Street Somewhere Here<br><span style="color:var(--brand)">●</span> 15 min &nbsp; 3.41 Km</div>
      </article>
      <article class="fav-card" style="left:117px;width:80px">
        <div class="photo photo-cafe" role="img" aria-label="Cafe interior with wooden tables"></div>
        <span class="mini-heart"></span><span class="mini-pill">100% Deposit Bonus</span>
        <div class="meta"><b>Leafbrew Elm Ridge</b><br>Tea · Bubble Tea · Burger<br><span style="color:var(--brand)">●</span> 123 A Street Somewhere Here<br><span style="color:var(--brand)">●</span> 15 min &nbsp; 3.41 Km</div>
      </article>
      <nav class="tabbar">
        <span class="tab active" style="left:30px"><svg class="icon" width="11" height="11"><use href="#i-home"/></svg>Home</span>
        <span class="tab" style="left:76px"><svg class="icon" width="11" height="11"><use href="#i-cart"/></svg>Cart</span>
        <span class="tab" style="left:113px"><svg class="icon" width="11" height="11"><use href="#i-doc"/></svg>Orders</span>
        <span class="tab" style="left:159px"><svg class="icon" width="11" height="11"><use href="#i-user"/></svg>Profile</span>
      </nav>
    </div>
  </section>

  <!-- Screen 2: Store -->
  <section class="device" style="left:664px;top:59px">
    <div class="screen">
      <div class="status"><span>9:41</span><svg class="icon" width="30" height="8" fill="#1e1e1e"><use href="#i-signal"/></svg></div>
      <div class="header-title">
        <span class="round-btn"><svg class="icon" width="10" height="10" color="#333"><use href="#i-back"/></svg></span>
        <h2>Leafbrew Elm Ridge</h2>
        <span class="round-btn"><svg class="icon" width="9" height="9" color="#333"><use href="#i-more"/></svg></span>
      </div>
      <div class="abs photo photo-cafe" style="left:8px;top:59px;width:174px;height:80px" role="img" aria-label="Store interior with wooden tables and pendant lights"></div>
      <div class="abs" style="left:83px;top:143px;width:24px;height:1.5px;background:#ddd"></div>
      <div class="abs" style="left:83px;top:143px;width:8px;height:1.5px;background:var(--brand)"></div>
      <div class="info-row" style="top:151px"><svg class="icon" width="7" height="7" color="var(--brand)"><use href="#i-store"/></svg>Leafbrew Elm Ridge</div>
      <div class="info-row" style="top:165px"><svg class="icon" width="7" height="7" color="var(--brand)"><use href="#i-pin"/></svg>Unit 12/40 Harbor St Elm Ridge WA 6050</div>
      <div class="info-row" style="top:179px"><svg class="icon" width="7" height="7" color="#f5b400"><use href="#i-star"/></svg>4.2 <span class="faint">( 1k+ Review)</span></div>
      <p class="section-title" style="top:194px">Category</p>
      <span class="chip filled" style="left:8px;top:213px;width:41px">Bubble Tea</span>
      <span class="chip" style="left:61px;top:213px;width:36px">Burger</span>
      <span class="chip" style="left:105px;top:213px;width:35px">Coffee</span>
      <span class="chip" style="left:148px;top:213px;width:35px">Snack</span>
      <p class="section-title" style="top:238px">Recommnded</p>
      <article class="menu-item" style="top:255px">
        <div class="photo photo-cup" role="img" aria-label="Cup of chocolate milk tea"></div>
        <span class="name">Milk Tea Coklat</span><span class="desc">Signature Milik Tea</span><span class="price">$6.00</span>
        <span class="rate"><svg class="icon" width="6" height="6" color="#f5b400"><use href="#i-star"/></svg>4.2</span><span class="fav-dot"></span>
      </article>
      <article class="menu-item" style="top:316px">
        <div class="photo photo-cup-amber" role="img" aria-label="Cup of original milk tea"></div>
        <span class="name">Milk Tea Original</span><span class="desc">Original Milik Tea</span><span class="price">$6.00</span>
        <span class="rate"><svg class="icon" width="6" height="6" color="#f5b400"><use href="#i-star"/></svg>4.2</span><span class="fav-dot"></span>
      </article>
      <article class="menu-item" style="top:372px">
        <div class="photo photo-cup-red" role="img" aria-label="Cup of red milk tea with soda"></div>
        <span class="name">Milk Tea Red</span><span class="desc">Jus Milik Tea With Soda</span><span class="price">$5.00</span>
        <span class="rate"><svg class="icon" width="6" height="6" color="#f5b400"><use href="#i-star"/></svg>4.2</span><span class="fav-dot"></span>
      </article>
    </div>
  </section>

  <!-- Screen 3: Order history, completed -->
  <section class="device" style="left:917px;top:59px">
    <div class="screen">
      <div class="status"><span>9:41</span><svg class="icon" width="30" height="8" fill="#1e1e1e"><use href="#i-signal"/></svg></div>
      <div class="header-title">
        <span class="round-btn"><svg class="icon" width="10" height="10" color="#333"><use href="#i-back"/></svg></span>
        <h2 style="font-size:11px">Order History</h2>
        <span class="round-btn"><svg class="icon" width="9" height="9" color="#333"><use href="#i-more"/></svg></span>
      </div>
      <div class="tabs"><span>Queue</span><span class="on">Completed</span></div>
      <article class="order-card" style="left:10px;top:104px;width:169px;height:90px">
        <div class="photo photo-cup" style="left:6px;top:6px" role="img" aria-label="Cup of chocolate milk tea"></div>
        <span class="name" style="left:57px;top:12px">Milk Tea Coklat</span>
        <span class="desc" style="left:57px;top:25px">Signature Milik Tea</span>
        <span class="price" style="left:57px;top:35px">$6.00 <span class="badge">Completed</span></span>
        <span class="btn outline" style="left:10px;top:67px;width:66px">Leave a Review</span>
        <span class="btn solid" style="left:85px;top:67px;width:76px">Order Again</span>
      </article>
      <nav class="tabbar">
        <span class="tab" style="left:30px"><svg class="icon" width="11" height="11"><use href="#i-home"/></svg>Home</span>
        <span class="tab" style="left:77px"><svg class="icon" width="11" height="11"><use href="#i-cart"/></svg>Cart</span>
        <span class="tab active" style="left:113px"><svg class="icon" width="11" height="11"><use href="#i-doc"/></svg>Orders</span>
        <span class="tab" style="left:159px"><svg class="icon" width="11" height="11"><use href="#i-user"/></svg>Profile</span>
      </nav>
    </div>
  </section>

  <!-- Screen 4: Order history, queue -->
  <section class="device" style="left:411px;top:546px">
    <div class="screen">
      <div class="status"><span>9:41</span><svg class="icon" width="30" height="8" fill="#1e1e1e"><use href="#i-signal"/></svg></div>
      <div class="header-title">
        <span class="round-btn"><svg class="icon" width="10" height="10" color="#333"><use href="#i-back"/></svg></span>
        <h2>Order History</h2>
        <span class="round-btn"><svg class="icon" width="9" height="9" color="#333"><use href="#i-more"/></svg></span>
      </div>
      <div class="tabs"><span class="on">Queue</span><span>Completed</span></div>
      <article class="order-card" style="left:16px;top:103px;width:162px;height:87px">
        <div class="photo photo-cup" style="left:1px;top:6px" role="img" aria-label="Cup of chocolate milk tea"></div>
        <span class="name" style="left:52px;top:12px">Milk Tea Coklat</span>
        <span class="desc" style="left:52px;top:24px">Signature Milik Tea</span>
        <span class="price" style="left:52px;top:35px">$6.00 <span class="badge">Paid</span></span>
        <span class="btn outline" style="left:5px;top:67px;width:60px">Cancle Order</span>
        <span class="btn solid" style="left:76px;top:67px;width:76px">Track Order</span>
      </article>
      <article class="order-card" style="left:16px;top:203px;width:162px;height:87px">
        <div class="photo photo-cup-amber" style="left:1px;top:6px" role="img" aria-label="Cup of caramel milk tea"></div>
        <span class="name" style="left:52px;top:12px">Milk Tea Caramel</span>
        <span class="desc" style="left:52px;top:24px">Signature Milik Tea Caramel</span>
        <span class="price" style="left:52px;top:35px">$2.00 <span class="badge">Paid</span></span>
        <span class="btn outline" style="left:5px;top:67px;width:60px">Cancle Order</span>
        <span class="btn solid" style="left:76px;top:67px;width:76px">Track Order</span>
      </article>
      <nav class="tabbar">
        <span class="tab" style="left:30px"><svg class="icon" width="11" height="11"><use href="#i-home"/></svg>Home</span>
        <span class="tab" style="left:76px"><svg class="icon" width="11" height="11"><use href="#i-cart"/></svg>Cart</span>
        <span class="tab active" style="left:117px"><svg class="icon" width="11" height="11"><use href="#i-doc"/></svg>Orders</span>
        <span class="tab" style="left:159px"><svg class="icon" width="11" height="11"><use href="#i-user"/></svg>Profile</span>
      </nav>
    </div>
  </section>

  <!-- Screen 5: Brand -->
  <section class="device" style="left:664px;top:546px">
    <div class="screen">
      <div class="status"><span>9:41</span><svg class="icon" width="30" height="8" fill="#1e1e1e"><use href="#i-signal"/></svg></div>
      <div class="header-title">
        <span class="round-btn"><svg class="icon" width="10" height="10" color="#333"><use href="#i-back"/></svg></span>
        <h2 style="font-size:11px">Leafbrew</h2>
        <span class="round-btn"><svg class="icon" width="9" height="9" color="#333"><use href="#i-more"/></svg></span>
      </div>
      <span class="arrow-btn" style="left:14px;top:93px;background:var(--brand-soft);color:var(--brand)"><svg class="icon" width="9" height="9"><use href="#i-chev-l"/></svg></span>
      <div class="brand-ring">Leafbrew</div>
      <span class="arrow-btn" style="left:160px;top:93px;background:var(--brand-bright);color:#fff"><svg class="icon" width="9" height="9"><use href="#i-chev-r"/></svg></span>
      <p class="section-title" style="top:170px">Stories Near You</p>
      <article class="story-card">
        <div class="photo photo-cafe" role="img" aria-label="Cafe interior with wooden tables"></div>
        <span class="heart-badge" style="left:5px;top:7px"></span>
        <span class="rate-badge" style="right:5px;top:7px"><svg class="icon" width="5" height="5" color="#f5b400"><use href="#i-star"/></svg>5.2</span>
        <span class="bonus-pill" style="left:5px;top:70px">100% Deposit Bonus</span>
        <div class="abs" style="left:6px;top:85px;display:flex;flex-direction:column;gap:3px">
          <b style="font-size:6px;font-weight:500">Cuppa Lane Central</b>
          <div class="tags"><span>Tea</span><span>Bubble Tea</span><span>Burger</span></div>
          <div class="loc" style="margin-top:3px"><svg class="icon" width="5" height="5" color="var(--brand)"><use href="#i-pin"/></svg>123 A Street Somewhere Here</div>
          <div class="eta"><svg class="icon" width="5" height="5" color="var(--brand)"><use href="#i-clock"/></svg>15 min &nbsp;&nbsp;&nbsp;&nbsp;<svg class="icon" width="5" height="5" color="var(--brand)"><use href="#i-map"/></svg>3.41 Km</div>
        </div>
      </article>
    </div>
  </section>

  <!-- Screen 6: Shop -->
  <section class="device" style="left:917px;top:546px">
    <div class="screen">
      <div class="status"><span>9:41</span><svg class="icon" width="30" height="8" fill="#1e1e1e"><use href="#i-signal"/></svg></div>
      <div class="header-greeting" style="left:7px">
        <div class="avatar" role="img" aria-label="User avatar photo"></div>
        <span class="greeting">Hii, Amir</span>
        <span class="round-btn"><svg class="icon" width="10" height="10" color="#333"><use href="#i-scan"/></svg></span>
        <span class="round-btn"><svg class="icon" width="10" height="10" color="#333"><use href="#i-wallet"/></svg></span>
      </div>
      <div class="search"><svg class="icon" width="8" height="8" color="#aaa"><use href="#i-search"/></svg>Find for food or restaurant...</div>
      <div class="filter-btn"><svg class="icon" width="10" height="10" color="var(--brand-bright)"><use href="#i-filter"/></svg></div>
      <p class="section-title" style="left:7px;top:93px">Category</p>
      <span class="chip plain" style="left:7px;top:112px;width:21px">Tea</span>
      <span class="chip plain" style="left:35px;top:112px;width:48px">Bubble Tea</span>
      <span class="chip plain" style="left:91px;top:112px;width:37px">Burger</span>
      <span class="chip plain" style="left:135px;top:112px;width:37px">Coffee</span>
      <span class="chip plain" style="left:180px;top:112px;width:20px"></span>
      <p class="section-title" style="left:7px;top:134px">Brand</p>
      <span class="brand-dot" style="left:7px;border:2px solid var(--brand);background:#fff" role="img" aria-label="Brand mark"></span>
      <span class="brand-dot" style="left:38px;border:3px solid #1f6fb8;background:#fff" role="img" aria-label="Brand mark"></span>
      <span class="brand-dot" style="left:69px;background:#243a8c" role="img" aria-label="Brand mark"></span>
      <span class="brand-dot" style="left:100px;border:3px solid #17956b;background:#fff" role="img" aria-label="Brand mark"></span>
      <span class="brand-dot" style="left:132px;background:#3d1f3a" role="img" aria-label="Brand mark"></span>
      <p class="section-title" style="left:7px;top:184px">Stories Near You</p>
      <p class="see-all" style="top:187px;right:9px">See All</p>
      <article class="store-row" style="top:203px">
        <div class="photo photo-cafe" role="img" aria-label="Cafe interior"></div>
        <span class="heart-badge"></span><span class="rate-badge">★ 4.2</span>
        <div class="body"><b>Demo 2 Eastvale</b><div class="tags"><span>Tea</span><span>Bubble Tea</span><span>Burger</span></div>
          <div class="loc"><svg class="icon" width="5" height="5" color="var(--brand)"><use href="#i-pin"/></svg>123 A Street Somewhere Here</div>
          <div class="eta"><svg class="icon" width="5" height="5" color="var(--brand)"><use href="#i-clock"/></svg>15 min &nbsp;&nbsp;<svg class="icon" width="5" height="5" color="var(--brand)"><use href="#i-map"/></svg>1.40 Km</div></div>
      </article>
      <article class="store-row" style="top:258px">
        <div class="photo photo-storefront" role="img" aria-label="Cafe interior with shelves"></div>
        <span class="heart-badge"></span><span class="rate-badge">★ 4.2</span>
        <div class="body"><b>Leafbrew Elm Ridge</b><div class="tags"><span>Tea</span><span>Bubble Tea</span><span>Burger</span></div>
          <div class="loc"><svg class="icon" width="5" height="5" color="var(--brand)"><use href="#i-pin"/></svg>Unit 12/40 Harbor St Elm Ridge WA 6050</div>
          <div class="eta"><svg class="icon" width="5" height="5" color="var(--brand)"><use href="#i-clock"/></svg>15 min &nbsp;&nbsp;<svg class="icon" width="5" height="5" color="var(--brand)"><use href="#i-map"/></svg>2.10 Km</div></div>
      </article>
      <article class="store-row" style="top:312px">
        <div class="photo photo-storefront" role="img" aria-label="Glass storefront of a tea shop"></div>
        <span class="heart-badge"></span><span class="rate-badge">★ 4.2</span>
        <div class="body"><b>Cuppa Lane Central</b><div class="tags"><span>Tea</span><span>Bubble Tea</span><span>Burger</span></div>
          <div class="loc"><svg class="icon" width="5" height="5" color="var(--brand)"><use href="#i-pin"/></svg>Unit 8 22 Central Ave Brookfield WA 6010</div>
          <div class="eta"><svg class="icon" width="5" height="5" color="var(--brand)"><use href="#i-clock"/></svg>15 min &nbsp;&nbsp;<svg class="icon" width="5" height="5" color="var(--brand)"><use href="#i-map"/></svg>3.41 Km</div></div>
      </article>
      <nav class="tabbar">
        <span class="tab" style="left:30px"><svg class="icon" width="11" height="11"><use href="#i-home"/></svg>Home</span>
        <span class="tab active" style="left:76px"><svg class="icon" width="11" height="11"><use href="#i-cart"/></svg>Cart</span>
        <span class="tab" style="left:114px"><svg class="icon" width="11" height="11"><use href="#i-doc"/></svg>Orders</span>
        <span class="tab" style="left:159px"><svg class="icon" width="11" height="11"><use href="#i-user"/></svg>Profile</span>
      </nav>
    </div>
  </section>
</main>
</body>
</html>
```